Wine label

I'm wanting to create a wine label that is very very simple, but eye catching. Jump off the shelf.

Name of Winery : Morrow Ridge

Nothing on the front but that - will be putting other info on back - which will be the brand label.

I was thinking of something MR - possibly - with morrow ridge intertwined. -

1 color label and possible 1 or 2 ink

```html
<!DOCTYPE html>
<html lang="en">
<head>
<meta charset="UTF-8">
<title>Morrow Ridge – Wine Label Options</title>
<link rel="stylesheet" href="https://fonts.googleapis.com/css2?family=Oswald:wght@500&family=Barlow:wght@500;600&display=swap">
<style>
  :root {
    --board: #d6d6d6;
    --sky: #1da7e8;
    --sky-deep: #22a9df;
    --cream: #fffef4;
    --paper: #ffffff;
    --ink: #1b1b1b;
    --caption: #ffffff;
    --rule: #9fd6ef;
  }
  * { margin: 0; padding: 0; box-sizing: border-box; }
  html, body { width: 1200px; height: 1000px; overflow: hidden; }
  body {
    background: var(--board);
    position: relative;
    font-family: "Barlow", "DIN Alternate", Arial, sans-serif;
  }
  .option-caption {
    position: absolute;
    top: 24px;
    font-family: "Oswald", "Arial Narrow", sans-serif;
    font-weight: 500;
    font-size: 30px;
    line-height: 40px;
    color: var(--caption);
  }
  .option-caption--left { left: 32px; }
  .option-caption--right { right: 27px; }

  .label {
    position: absolute;
    top: 111px;
    width: 574px;
    height: 858px;
    box-shadow: 0 2px 6px rgba(0,0,0,0.35);
  }
  .label--blue { left: 18px; background: var(--sky); }
  .label--white { left: 608px; background: var(--paper); }

  .label__panel {
    position: absolute;
    left: 43px;
    top: 186px;
    width: 488px;
    height: 488px;
  }
  .label--blue .label__panel { background: var(--cream); }
  .label--white .label__panel { background: var(--sky-deep); }

  .monogram {
    position: absolute;
    left: 0; right: 0;
    top: 150px;
    text-align: center;
    font-weight: 600;
    font-size: 150px;
    line-height: 180px;
    letter-spacing: 2px;
  }
  .label--blue .monogram { color: var(--sky); }
  .label--white .monogram { color: var(--ink); }

  .label__name--stacked {
    position: absolute;
    right: 13px;
    top: 392px;
    text-align: right;
    font-weight: 500;
    font-size: 33px;
    line-height: 46px;
    letter-spacing: 4px;
    color: var(--sky);
  }

  .label__fold {
    position: absolute;
    left: 0;
    top: 717px;
    width: 552px;
    height: 2px;
    background: rgba(255,255,255,0.35);
  }

  .label__rule {
    position: absolute;
    left: 0;
    top: 717px;
    width: 560px;
    height: 1px;
    background: var(--rule);
  }
  .label__name--spread {
    position: absolute;
    left: 0;
    width: 574px;
    top: 694px;
    text-align: center;
    font-weight: 500;
    font-size: 34px;
    line-height: 44px;
    letter-spacing: 22px;
    padding-left: 22px;
    color: var(--sky);
    white-space: nowrap;
  }
  .label__name--spread span {
    background: var(--paper);
  }
</style>
</head>
<body>
  <div class="option-caption option-caption--left">option 1</div>
  <div class="option-caption option-caption--right">option 2</div>

  <section class="label label--blue" aria-label="Label option 1">
    <div class="label__panel">
      <div class="monogram">MR</div>
      <p class="label__name--stacked">Morrow<br>Ridge</p>
    </div>
    <div class="label__fold"></div>
  </section>

  <section class="label label--white" aria-label="Label option 2">
    <div class="label__panel">
      <div class="monogram">MR</div>
    </div>
    <div class="label__rule"></div>
    <p class="label__name--spread"><span>Morrow Ridge</span></p>
  </section>
</body>
</html>
```